Webdesign für Ingenieurbüro
Zielgruppe
Ingenieurbüro Dravotek GmbH
Leistungen:
Siedlungswasserwirtschaft
Straßen- und Ingenieurbau
Hochwasserschutz / Wasserbau
Pegelanlagen
Komplexerschließungen
Koordinierung nach BaustellV
Landschaftsbau
Zielgruppe ist die Öffentliche Hand
Aufgabenstellung
Leistungsbereiche und Stellenangebote (zZt. 3 Stück) sollen zu gleichen Teilen im Fokus stehen. Call to action zum Berweberformular ist nötig.
Zu beachten wäre, dass das Unternehmen für öffentliche Auftraggeber arbeitet. Die Seite sollte klar strukturiert und seriös wirken.
Der Login-Bereich soll in den Hintergrund treten, eventuell über dem footer.
Logo aus dem Cover - siehe anbei übernehmen

```html
<!DOCTYPE html>
<html lang="de">
<head>
<meta charset="utf-8">
<title>Ingenieurbüro Dravotek GmbH</title>
<link href="https://fonts.googleapis.com/css2?family=Open+Sans:wght@400;600;700&family=Arimo:wght@400&display=swap" rel="stylesheet">
<style>
:root{
  --navy:#2b3a9a;
  --footer:#2e4196;
  --cyan:#00b3e8;
  --sky:#45c6ee;
  --button:#3d4a57;
  --text:#222;
  --line:#bfe3f3;
  --white:#fff;
}
*{box-sizing:border-box;margin:0;padding:0}
html,body{width:960px;height:1200px;overflow:hidden;background:#fff}
.stage{position:relative;width:960px;height:1200px;overflow:hidden}
.page{position:absolute;left:298px;top:32px;width:658px;height:2060px;background:var(--white);
  transform:scale(.5587);transform-origin:0 0;box-shadow:0 0 18px rgba(0,0,0,.35);
  font-family:"Open Sans",sans-serif;color:var(--text)}
.abs{position:absolute}
.brand{left:62px;top:38px;display:flex;align-items:center;gap:8px;color:var(--navy);font-weight:700;font-size:19px}
.brand-dot{width:22px;height:22px;border-radius:50%;background:var(--navy)}
.nav{left:237px;top:67px;display:flex;gap:8px;font-size:9px;letter-spacing:.2px}
.nav span{padding:3px 3px;line-height:10px}
.nav .active{background:var(--navy);color:#fff}
.hero{left:0;top:98px;width:658px;height:183px;background:linear-gradient(110deg,#b9bcc0,#dcdee0 45%,#c4c7ca 70%,#6f757b)}
.headline{left:60px;top:286px;width:538px;text-align:center;font-weight:700;font-size:21.5px;line-height:25px;color:var(--navy)}
.career{left:172px;top:381px;width:314px;height:172px}
.career-img{height:123px;background:linear-gradient(135deg,#5e7f88,#8aa3a8 50%,#c9d4d6);display:flex;align-items:center;justify-content:center;text-align:center;color:#fff;font-weight:600;font-size:19px;line-height:20.5px;padding:0 30px}
.career-btn{height:49px;background:var(--cyan);color:#fff;font-weight:600;font-size:17px;display:flex;align-items:center;justify-content:center}
.section-title{color:var(--navy);font-size:20px;font-weight:400;text-align:center;width:658px;left:0}
.services{left:255px;top:619px;list-style:none;font-family:Arimo,sans-serif;font-size:11px;line-height:14.7px;color:#111}
.services li{position:relative;padding-left:12px}
.services li::before{content:"";position:absolute;left:0;top:4px;width:6px;height:6px;background:var(--cyan)}
.divider{left:0;top:778px;width:658px;height:1px;background:var(--line)}
.about{left:95px;top:829px;width:460px;text-align:center;font-family:Arimo,sans-serif;font-size:13px;line-height:16.6px;color:#222}
.contact{left:0;top:976px;width:658px;height:371px;background:var(--sky);color:#fff}
.find{left:28px;top:14px;font-size:15px}
.address{left:27px;top:43px;font-size:13px;line-height:19.5px}
.map{left:27px;top:133px;width:321px;height:184px;background:linear-gradient(135deg,#eef0f2,#e3e6ea)}
.ktitle{left:396px;top:14px;font-size:20px;font-weight:700}
.ksub{left:400px;top:41px;font-size:11px}
.field{background:#fff;color:#666;font-size:8px;padding:9px 6px;width:177px}
.check{left:398px;top:296px;width:9px;height:9px;background:#fff}
.checktext{left:417px;top:292px;font-size:8.5px;line-height:12.5px;width:160px}
.send{left:431px;top:328px;width:126px;height:26px;border-radius:13px;background:var(--button);color:#fff;font-size:8.5px;display:flex;align-items:center;justify-content:center}
.projects-title{left:0;top:1402px;width:622px;text-align:center;color:var(--navy);font-size:15px}
.thumb{top:1439px;width:137px;height:78px}
.thumb span{position:absolute;bottom:4px;width:100%;text-align:center;font-size:4.5px;color:#fff}
.dot{top:1528px;width:10px;height:10px;border-radius:50%;border:1px solid #999}
.dot.on{background:var(--cyan);border-color:var(--cyan)}
.login-title{left:0;top:1606px;width:668px;text-align:center;color:var(--navy);font-size:15px}
.login-field{left:233px;width:200px;height:24px;border:1px solid #888;font-size:15px;padding:0 6px;line-height:22px;color:#111}
.forgot{left:233px;top:1753px;width:200px;text-align:right;font-size:15px;color:#111}
.footer{left:0;top:1854px;width:658px;height:206px;background:var(--footer);color:#fff;font-family:Arimo,sans-serif}
.f-address{left:40px;top:37px;font-size:11px;line-height:14.7px}
.social{top:65px;width:30px;height:30px;border-radius:50%;background:#fff}
.f-links{left:500px;top:64px;font-size:11px;line-height:17px}
.copyright{left:500px;top:180px;font-size:9.5px}
</style>
</head>
<body>
<div class="stage">
<div class="page">
  <header>
    <div class="abs brand"><span class="brand-dot"></span>Dravotek</div>
    <nav class="abs nav"><span class="active">HOME</span><span>LEISTUNGEN</span><span>KARRIERE</span><span>UNTERNEHMEN</span><span>PROJEKTE</span><span>KONTAKT</span></nav>
  </header>
  <div class="abs hero" role="img" aria-label="Foto: Messschieber und Werkzeug auf technischen Zeichnungen"></div>
  <h1 class="abs headline">Dravotek GmbH ist Ihr kompetenter und zuverlässiger Partner mit langjähriger Erfahrung im öffentlichen Bereich</h1>

  <div class="abs career">
    <div class="career-img" role="img" aria-label="Foto: Hand mit Stift über einem Plan">Starten Sie Ihre Karriere jetzt! Werden Sie ein Dravotekianer!</div>
    <div class="career-btn">zu den Stellangeboten</div>
  </div>

  <h2 class="abs section-title" style="top:582px">UNSERE LEISTUNGEN</h2>
  <ul class="abs services">
    <li>Siedlungswasserwirtschaft</li>
    <li>Straßen- und Ingenieurbau</li>
    <li>Hochwasserschutz / Wasserbau</li>
    <li>Pegelanlagen</li>
    <li>Komplexerschließungen</li>
    <li>Koordinierung nach BaustellV</li>
    <li>Landschaftsbau</li>
  </ul>
  <div class="abs divider"></div>

  <h2 class="abs section-title" style="top:793px;width:610px">ÜBER UNS</h2>
  <p class="abs about">Unser Ingenieurbüro DRAVOTEK GmbH ist ein mittelständischen Unternehmen, welches 1991 gegründet wurde. Seit 25 Jahren bieten wir Ingenieurleistungen an. Wir sind ein zuverlässiger Partner für fachgerechte Beratung, Planung und Bauüberwachung von Maßnahmen des Tief-, Wasser- und Straßenbaues. Hierfür sind 18 hochqualifizierte und engagierte Ingenieure und technische Mitarbeiter verantwortlich. Modernste Kommunikationstechnik und Spezialsoftware, sowie die Kreativität der Mitarbeiter sind ein Garant für effektive Lösungen.</p>

  <section class="abs contact">
    <div class="abs find">So finden Sie uns</div>
    <div class="abs address">Ingenieurbüro Dravotek GmbH<br>Lindenauer Straße 148<br>09113 Talheim</div>
    <div class="abs map" role="img" aria-label="Stadtplan mit Standortmarkierung des Büros"></div>
    <div class="abs ktitle">KONTAKT</div>
    <div class="abs ksub">Senden Sie eine Nachricht!</div>
    <div class="abs field" style="left:398px;top:77px;height:28px">Ihre Email</div>
    <div class="abs field" style="left:398px;top:132px;height:28px">Betreff</div>
    <div class="abs field" style="left:398px;top:192px;height:92px;padding-top:14px">Ihre Nachricht</div>
    <div class="abs check"></div>
    <div class="abs checktext">Ich habe die Datenschutzerkleräung gelesen...</div>
    <div class="abs send">Nachricht absenden</div>
  </section>

  <h2 class="abs projects-title">Realisierte Projekte</h2>
  <div class="abs thumb" style="left:42px;background:linear-gradient(160deg,#5a4a3a,#c9ccd2 55%,#6e6454)" role="img" aria-label="Projektfoto: Gewässerausbau im Winter"><span>Gewässerausbau Nordbach</span></div>
  <div class="abs thumb" style="left:185px;background:linear-gradient(160deg,#4f6a3a,#a9b0ad 55%,#6d7a58)" role="img" aria-label="Projektfoto: renaturierter Bachlauf"><span>Gewässerausbau Nordbach</span></div>
  <div class="abs thumb" style="left:327px;background:linear-gradient(160deg,#2f4a22,#6f8f4a 55%,#3e5a2a)" role="img" aria-label="Projektfoto: Brücke im Park"><span>Uferweg</span></div>
  <div class="abs thumb" style="left:469px;background:linear-gradient(160deg,#8a9096,#b8bcc0 55%,#7b8086)" role="img" aria-label="Projektfoto: Bauarbeiten an einer Ufermauer"><span>Uferweg</span></div>
  <div class="abs dot on" style="left:297px"></div>
  <div class="abs dot" style="left:319px"></div>
  <div class="abs dot" style="left:341px"></div>

  <h2 class="abs login-title">INTERNER KUNDENBEREICH</h2>
  <div class="abs login-field" style="top:1643px">Kundennummer</div>
  <div class="abs login-field" style="top:1685px">Passwort</div>
  <div class="abs login-field" style="top:1727px">LOGIN</div>
  <div class="abs forgot">Passwort vergessen</div>

  <footer class="abs footer">
    <div class="abs f-address">Ingenieurbüro Dravotek GmbH<br>Lindenauer Straße 148<br>09113 Talheim<br>Tel.0371 / 64302-0<br>Fax:0371 / 64302-43<br>ingenieurbuero@dravotek.de</div>
    <div class="abs social" style="left:314px" aria-label="Soziales Netzwerk"></div>
    <div class="abs social" style="left:364px" aria-label="Soziales Netzwerk"></div>
    <div class="abs f-links">Impressum<br>Datenschutz</div>
    <div class="abs copyright">Copyright Dravotek GmbH 2021</div>
  </footer>
</div>
</div>
</body>
</html>
```